Rock Star Designer Needed

I'm looking for a similar wordpress design to the examples below...

I really like the simple, clean design of these example
- http://quillharborguild.net
- http://hub.brightmarrowtips.net

What I like are the simple design ad for webinar at top/bottom and spot for content in the middle.

I specifically like the font on the graphical looking banners from the 2nd site (http://hub.brightmarrowtips.net)

This will be the home of our NEW site at http://www.PebbleLanternSeminarVault.net

Looking for a fun youthful look, inspired by sales letters found at tally grove.

Are you up to the challenge?

Target Market(s)

Internet Marketers, People Looking To Make Money Online

Requirements
Must have
• Real easy to see template style by viewing...
http://quillharborguild.net/

Main Section (Left under header)
- Graphic Section (could be said to be ads) at Top & Bottom of blog - Content Section (text) In the middle (graphic section)
Sidebar (Right side of blog)
- Optin on Top Left of blog sidebar
- Graphic (could be said to be ad) underneath optin
- Categories section under graphic

```html
<!DOCTYPE html>
<html lang="en">
<head>
<meta charset="utf-8">
<title>Pebble Lantern Seminar Vault</title>
<link rel="stylesheet" href="https://fonts.googleapis.com/css2?family=Arimo:wght@400;700&display=swap">
<style>
:root{
  --orange:#f6a50a;
  --orange-light:#ffd23a;
  --green:#4cc41a;
  --green-light:#b8ee5a;
  --tab-yellow:#ffd86a;
  --red:#e0201c;
  --navy:#0a3a9c;
  --teal:#94cfd0;
  --teal-dark:#6fb3b5;
  --cream:#ffe4a0;
  --gold:#f8b320;
  --grey-text:#555;
  --dark:#222;
  --line:#bbb;
}
*{box-sizing:border-box;margin:0;padding:0}
html,body{width:1200px;height:2345px;overflow:hidden;background:#fff;font-family:"Arimo",Arial,sans-serif;color:var(--dark)}
.page{position:relative;width:1200px;height:2345px}
.abs{position:absolute}
.site-header{left:0;top:0;width:1200px;height:176px;background:linear-gradient(#ffdd2a,var(--orange))}
.brand{left:0;top:40px;width:1200px;text-align:center}
.brand-name{font-size:44px;font-weight:700;color:#1c5fc4;display:inline-flex;align-items:center;gap:16px}
.brand-name .dot{width:30px;height:30px;border-radius:50%;background:#1c5fc4;display:inline-block}
.brand-tag{font-size:22px;font-weight:700;color:#1c5fc4;margin-top:8px}
.steps{left:0;top:176px;width:1200px;height:58px;background:linear-gradient(var(--green-light),var(--green));display:flex;padding-left:246px}
.step{width:230px;height:58px;line-height:58px;text-align:center;font-size:18px;font-weight:700;border-right:1px solid #9ad85a}
.step.is-active{background:var(--tab-yellow)}
.ad{border:1px solid #999}
.ad-top{left:43px;top:264px;width:1096px;height:117px;background:linear-gradient(90deg,#1e7a2c 0 62%,#e08a2a 62%,#b8581a)}
.ad-side{left:39px;top:670px;width:260px;height:229px;background:linear-gradient(135deg,#fff 0 40%,#e86a28 40% 60%,#5bb6a0 60%)}
.ad-bottom{left:39px;top:2099px;width:1100px;height:119px;background:linear-gradient(90deg,#c8202c 0 8%,#f2d23a 8% 78%,#f8e070)}
.optin{left:39px;top:430px;width:260px;height:215px;border:2px solid #ccc}
.optin h3{background:#ddd;font-size:17px;padding:8px 14px}
.optin ol{list-style:none;padding:12px 16px;font-size:16px;line-height:30px}
.cat-head{left:39px;top:938px;width:260px;height:43px;background:var(--navy);color:#fff;font-size:20px;font-weight:700;padding:10px 24px}
.categories{left:39px;top:991px;width:260px;height:344px;background:var(--teal);border-radius:8px;list-style:none;padding:8px 16px;box-shadow:0 2px 4px rgba(0,0,0,.3)}
.categories li{font-size:17px;padding:16px 0 15px;border-bottom:1px solid var(--teal-dark)}
.categories li:last-child{border:0}
.reg-head{left:883px;top:430px;width:258px;height:43px;background:var(--navy);color:#fff;font-size:20px;font-weight:700;padding:10px 20px}
.reg-box{left:883px;top:489px;width:258px;height:254px;background:var(--teal);border-radius:10px;padding:26px 18px;box-shadow:0 3px 5px rgba(0,0,0,.35);font-size:17px}
.reg-box .select{height:28px;background:#fff;border:1px solid #888;margin:12px 0 6px;position:relative}
.reg-box .select span{position:absolute;right:0;top:0;width:24px;height:26px;background:#ddd;border-left:1px solid #888}
.reg-box .note{font-size:11px}
.reg-box .note s{color:#666}
.reg-box a{display:block;color:var(--navy);font-size:14px;font-weight:700;text-decoration:none;margin:18px 0 22px;line-height:20px}
.btn{display:block;text-align:center;background:linear-gradient(#ffd25a,var(--gold));border:1px solid #e0900a;border-radius:8px;font-weight:700;color:var(--dark);box-shadow:0 2px 3px rgba(0,0,0,.3)}
.reg-box .btn{width:200px;margin:0 auto;height:36px;line-height:34px;font-size:18px}
.center{text-align:center}
.headline{left:313px;top:445px;width:570px;color:var(--red);font-size:29px;font-weight:700;line-height:33px}
.subhead{left:313px;top:598px;width:570px;font-size:18px;font-weight:700;line-height:26px;color:#333}
.alert{left:313px;top:709px;width:557px;height:251px;border:2px solid #ccc;padding:18px 20px}
.alert h2{color:var(--red);font-size:26px;margin-bottom:12px}
.alert p{font-size:18px;font-weight:700;line-height:26px}
.alert h3{color:var(--red);font-size:26px;line-height:30px;margin-top:14px}
.benefits{left:313px;top:987px;width:570px;font-size:14px;font-weight:700;color:var(--grey-text);line-height:18px}
.benefits>p{padding-left:24px;margin-bottom:14px}
.benefits ul{list-style:none}
.benefits li{position:relative;padding-left:26px;margin-bottom:16px}
.benefits li::before{content:"";position:absolute;left:0;top:4px;width:10px;height:10px;border-radius:50%;background:#666}
.callout{left:299px;top:1380px;width:584px;height:156px;background:var(--cream);border-radius:10px;color:var(--red);font-size:27px;font-weight:700;line-height:35px;padding:14px 20px}
.plus{left:299px;top:1557px;width:584px;font-size:15px;color:var(--grey-text);line-height:25px}
.insider{left:299px;top:1628px;width:584px;height:166px;background:linear-gradient(var(--green-light),var(--green));border-radius:8px;font-size:26px;font-weight:700;line-height:46px;padding:18px 26px}
.arrow{left:510px;top:1794px}
.how{left:299px;top:1895px;width:584px}
.how h2{font-size:38px}
.how p{font-size:16px;margin-top:10px}
.how .red{color:var(--red);font-weight:700;margin-top:6px}
.btn-main{left:440px;top:2017px;width:318px;height:58px;line-height:56px;font-size:29px}
.site-footer{left:0;top:2247px;width:1200px;height:98px;background:var(--orange);color:#fff;font-size:13px;text-align:center;padding-top:18px;line-height:40px}
</style>
</head>
<body>
<div class="page">
  <header class="site-header abs">
    <div class="brand abs">
      <div class="brand-name"><span class="dot"></span>Pebble Lantern Seminar Vault</div>
      <div class="brand-tag">Your Blueprint To Wealth &amp; Freedom</div>
    </div>
  </header>
  <nav class="steps abs">
    <div class="step is-active">1. Choose Date</div>
    <div class="step">2. Choose Time</div>
    <div class="step">3. Get Free Bonus</div>
  </nav>

  <div class="ad ad-top abs" role="img" aria-label="Gourdhaven fall family fun banner with a field of pumpkins"></div>

  <aside class="optin abs">
    <h3>Option box</h3>
    <ol>
      <li>1. Lorem Ipsum is simply</li>
      <li>2. Lorem Ipsum is simply</li>
      <li>3. Lorem Ipsum is simply</li>
      <li>4. Lorem Ipsum is simply</li>
      <li>5. Lorem Ipsum is simply</li>
    </ol>
  </aside>
  <div class="ad ad-side abs" role="img" aria-label="Larkmoor store sale ad showing a red stand mixer, lowest prices of the season, free shipping"></div>
  <div class="cat-head abs">Categories</div>
  <ul class="categories abs">
    <li>About</li><li>Case Studies</li><li>Increased Learning</li><li>Categories</li><li>The FREE Webinar</li><li>Uncategorized</li>
  </ul>

  <div class="reg-head abs">Register Free Now</div>
  <div class="reg-box abs">
    <strong>Choose a date:</strong>
    <div class="select"><span></span></div>
    <div class="note">(Only <s>300</s> 70 seats left for this event time.)</div>
    <a>Register for Watching<br>Yesterday's Replay</a>
    <span class="btn">Reserve My Spot!</span>
  </div>

  <main>
    <h1 class="headline abs center">NEW Game Changing System That Converts Prospects Into Custom-ers On Autopilot...<br>Yes, Even While You Sleep!</h1>
    <p class="subhead abs center">The "Big Dawg" Marketers Use This System to Capture HUGE Market Share and More Cash on Auto-Pilot Everyday!</p>
    <section class="alert abs center">
      <h2>Urgent Alert: Only 70 Seats Available!</h2>
      <p>Two Young "Secret Weapon" Multi- Millionaires<br>From Florida Change the Game and Unleash:</p>
      <h3>A New, Plug-In-And-Play Webinar System With The Potential To Explode Your Biz Cash-Flow Almost Overnight!</h3>
    </section>
    <section class="benefits abs">
      <p>During This FREE Webinar you'll find out exactly how you can:</p>
      <ul>
        <li>Discover a proven 12 step system you can use to build killer webinar presentations for maximum response and high conversions...in any customer base you want to capture and dominate!</li>
        <li>Gain the five simple steps with the power to transform automated webinars into your reliable, cash-pulling bullet train...running day and night.</li>
        <li>Learn how online and offline business owners with NO prior experience are using this amazing system to generate almost "instant" cash-flow in less than 24 hours...</li>
        <li>How to cash in on a HOT gold rush NOW through the top sources for quality buyer traffic...and dozens of ways you can drive them to your webinars!</li>
        <li>Get the full story how two newbie entrepreneurs built multi-millions in wealth with mega-successful webinar campaigns...and how you can do it today!</li>
      </ul>
    </section>
    <div class="callout abs center">Let Pebble Lantern Seminar Vault do all the work for you... while you gain new customers like crazy and generate a terrific income!</div>
    <p class="plus abs center">Plus tons more...jump on it now, we only have 70 front-row<br>seats available, reserve your seat right now...</p>
    <div class="insider abs center">Be one of the "insiders" who will have full access to a fresh way to explode your biz! - get fully registered below...</div>
    <svg class="arrow abs" width="162" height="82" viewBox="0 0 162 82"><polygon points="40,0 122,0 122,22 162,22 81,82 0,22 40,22" fill="#4cc41a"/></svg>
    <section class="how abs center">
      <h2>How do I Register</h2>
      <p>Its easy... just choose the webinar time above</p>
      <p class="red">The first 300 To Register will Get in Free</p>
    </section>
    <span class="btn btn-main abs">Reserve My Spot!</span>
  </main>

  <div class="ad ad-bottom abs" role="img" aria-label="wander&amp;wonder kids discovery hall banner with a smiling sun illustration and click tab"></div>

  <footer class="site-footer abs">
    Terms of Use | Disclaimer | Privacy Policy<br>
    Copyright © 2012 by Pebble Lantern Seminar Vault. All Rights Reserved.
  </footer>
</div>
</body>
</html>
```